The Willow Hours - a modern wellness brand

Looking for a modern, simple, and clean website for a virtual consulting firm focused on holistic wellness and sustainable living. Want a strong combo of text and photos (really shitty starts are available for reference on www.thewillowhours.com and www.helenabrusco.com for reference - general idea is in the right direction, was too difficult to work through with the wordpress template and nothing laid out correctly)
Needs include:
- strong home / landing page
- ability to schedule (use calend.ly) on the site
- online shop / purchasing POS integration
- blog
-multiple 'services' pages
- about page
- contact page
(attached brand board images for brand style / reference)
Updates
Want more opportunity for designs and feedback
Target Market(s)
women and gay men aged 30-50
Coding
Coded - Design and coding required
Number of Pages Required
5+ page
Colors
Designer to choose only greyscale colors for use in the design.
Requirements
Must have
- the ability for me to update and manage through wordpress when things like pricing, or services change
Should not have
- complicated anything

```html
<!DOCTYPE html>
<html lang="en">
<head>
<meta charset="utf-8">
<title>The Willow Hours</title>
<link href="https://fonts.googleapis.com/css2?family=Marcellus&family=Jost:wght@300;400;500;600&family=Roboto:wght@400;500&display=swap" rel="stylesheet">
<style>
:root{
  --plum:#2e1a4a;
  --ink:#1f1f24;
  --body:#5d5d63;
  --light:#f7f7f7;
  --cream:#f4f1ec;
  --white:#ffffff;
  --line:#c9c9cc;
}
*{box-sizing:border-box;margin:0;padding:0}
html,body{width:1200px;height:3632px;overflow:hidden}
body{position:relative;font-family:'Jost',sans-serif;color:var(--ink);background:var(--white)}
.abs{position:absolute}
.serif{font-family:'Marcellus',serif}
.accent{color:var(--plum)}

/* hero */
.hero{position:absolute;left:0;top:0;width:1200px;height:625px;
  background:linear-gradient(180deg,#6e4b45 0%,#8a5c3c 35%,#b07a3a 60%,#8d5a22 100%)}
.hero-photo{position:absolute;inset:0;background:radial-gradient(ellipse at 60% 35%,rgba(240,190,120,.45),transparent 60%)}
.nav{position:absolute;top:28px;left:0;width:1200px;height:24px;font-size:16px;color:var(--white);letter-spacing:.3px}
.nav a{position:absolute;color:var(--white);text-decoration:none}
.nav a.active{border-bottom:1px solid var(--white);padding-bottom:3px}
.nav .sep{position:absolute}
.brand-mark{left:527px;top:178px;width:146px;height:146px;border:2px solid rgba(255,255,255,.85);border-radius:50%}
.brand-name{left:0;width:1200px;top:352px;text-align:center;font-family:'Marcellus',serif;font-size:46px;letter-spacing:12px;color:var(--white)}
.btn-outline{display:flex;align-items:center;justify-content:center;border:1.5px solid var(--white);border-radius:20px;color:var(--white);font-weight:500}
.hero .btn-outline{left:504px;top:463px;width:192px;height:39px;font-size:15px}

/* about */
.about-photo{left:144px;top:711px;width:384px;height:384px;border-radius:50%;
  background:linear-gradient(135deg,#7a3a3a 0%,#c0875a 45%,#e3a43a 70%,#3d3f6a 100%)}
.about-title{left:611px;top:736px;font-size:41px}
.about-text{left:611px;top:790px;width:464px;font-size:14.5px;line-height:25.6px;color:var(--body);font-weight:300;text-align:justify}
.about-text p+p{margin-top:7px}
.btn-solid{display:flex;align-items:center;justify-content:center;background:var(--plum);color:var(--white);border-radius:20px;font-size:15px;font-weight:500}
.about .btn-solid{left:611px;top:1021px;width:156px;height:40px}

/* services */
.services{position:absolute;left:0;top:1175px;width:1200px;height:1060px;background:var(--light)}
.section-title{position:absolute;left:0;width:1200px;text-align:center;font-family:'Marcellus',serif;font-size:41px}
.card-photo{position:absolute;width:474px;height:339px}
.card-title{position:absolute;font-size:29px;font-weight:400;color:var(--ink)}

/* testimonial */
.quote{left:210px;top:2384px;width:780px;font-family:'Roboto',sans-serif;font-size:17px;line-height:32px;text-align:justify;text-align-last:center;color:var(--ink)}
.avatar{left:517px;top:2532px;width:44px;height:44px;border-radius:50%;background:linear-gradient(135deg,#9bb0c4,#5a6f86)}
.author{left:571px;top:2534px;font-family:'Roboto',sans-serif;font-size:18px;font-weight:500}
.author small{display:block;font-size:12px;font-weight:400;margin-top:1px}
.dot-bar{position:absolute;top:2609px;height:2px;background:var(--line)}
.dot-bar.on{background:var(--plum)}

/* contact */
.contact{position:absolute;left:0;top:2705px;width:1200px;height:595px;overflow:hidden}
.contact-bg{position:absolute;inset:0;
  background:radial-gradient(ellipse at 75% 90%,#4a3520 0%,#1e1c1e 45%,#141316 100%)}
.contact-title{top:74px;font-size:36px;color:var(--white)}
.contact-lead{left:0;width:1200px;top:124px;text-align:center;color:var(--white);font-size:19px;font-weight:500}
.contact-sub{left:320px;width:560px;top:159px;text-align:center;color:var(--white);font-size:15px;line-height:27px;font-weight:300}
.field{position:absolute;background:var(--white);font-size:15px;color:#555;padding:11px 11px;font-weight:300}
.radio{position:absolute;top:305px;color:var(--white);font-size:16px;font-weight:300;display:flex;align-items:center;gap:8px}
.radio i{width:14px;height:14px;border-radius:50%;background:var(--white);display:block}
.contact .btn-outline{left:522px;top:472px;width:156px;height:40px;font-size:16px;font-weight:600}

/* footer */
.footer{position:absolute;left:0;top:3300px;width:1200px;height:332px;background:var(--cream)}
.foot-mark{left:107px;top:3355px;width:80px;height:80px;border:1.5px solid #555;border-radius:50%}
.foot-name{left:206px;top:3381px;font-family:'Marcellus',serif;font-size:22px;letter-spacing:5px;color:var(--ink);white-space:nowrap}
.social{position:absolute;top:3451px;width:42px;height:42px;border:1.5px solid var(--plum);border-radius:50%}
.foot-col{position:absolute;top:3345px;font-size:15px;line-height:28px;color:#4a4a50;font-weight:300}
.foot-col h4{font-weight:400;color:var(--ink);font-size:16px;line-height:28px}
.foot-col .row{display:flex;gap:7px;align-items:flex-start}
.foot-col svg{margin-top:4px;flex:none}
.foot-rule{left:107px;top:3572px;width:998px;height:1px;background:#9a9a9a}
.copyright{left:0;width:1200px;top:3591px;text-align:center;font-size:14px;color:#4a4a50;font-weight:300}
</style>
</head>
<body>

<header class="hero">
  <div class="hero-photo" role="img" aria-label="Woman in a long dress walking through a golden wheat field at sunset"></div>
  <nav class="nav">
    <a class="active" href="#" style="left:261px">HOME</a><span class="sep" style="left:341px">|</span>
    <a href="#" style="left:378px">ABOUT</a><span class="sep" style="left:464px">|</span>
    <a href="#" style="left:500px">SHOP</a><span class="sep" style="left:575px">|</span>
    <a href="#" style="left:610px">BLOG</a><span class="sep" style="left:686px">|</span>
    <a href="#" style="left:723px">SERVICES</a><span class="sep" style="left:825px">|</span>
    <a href="#" style="left:861px">CONTACT</a>
  </nav>
  <div class="abs brand-mark"></div>
  <div class="abs brand-name">THE WILLOW HOURS</div>
  <a class="abs btn-outline">Book an Appointment</a>
</header>

<section class="about">
  <svg class="abs" style="left:124px;top:691px" width="424" height="424" viewBox="0 0 424 424" aria-hidden="true">
    <circle cx="212" cy="212" r="205" fill="none" stroke="#111" stroke-width="7" stroke-linecap="round" stroke-dasharray="0 15"/>
  </svg>
  <div class="abs about-photo" role="img" aria-label="Two women sharing a tender embrace"></div>
  <h2 class="abs about-title serif">ABOUT <span class="accent">US</span></h2>
  <div class="abs about-text">
    <p>Sed ut perspiciatis unde omnis iste or sit voluptatem accusantium doloremque laudantium, totam rem aperiam, eaque ipsa quae ab illo inventore veritatis et quasito beatae vitae dicta sunt explicabo. Nemo enim ipsam voluptatem sit aspernatur aut odit aut fugit, sed quia consequuntur magni dolores eos ui ratione voluptatem sequi nesciunt.</p>
    <p>Lorem ipsum dolor sit amet, consectetur adipiscing elit, sed do eiusmod tempor incididunt ut labore et dolore magna aliqua. Ut enim ad minim veniam, quis nostrud exercitation ullamco</p>
  </div>
  <a class="abs btn-solid">Learn More</a>
</section>

<section class="services">
  <h2 class="section-title" style="top:88px">OUR <span class="accent">SERVICES</span></h2>
  <div class="card-photo" style="left:110px;top:169px;background:linear-gradient(135deg,#e9eef0,#c7dcd8 45%,#f1e9c8 60%,#8fa3b8)" role="img" aria-label="Woman relaxing on a treatment table during an energy healing session"></div>
  <div class="card-title" style="left:107px;top:518px">Finibus Bonorum et</div>
  <div class="card-photo" style="left:615px;top:169px;background:linear-gradient(160deg,#3f4a2e,#6d6a4e 45%,#5a6870 70%,#2f3a2a)" role="img" aria-label="Living root bridge spanning a forest stream"></div>
  <div class="card-title" style="left:613px;top:518px">Finibus Bonorum et</div>
  <div class="card-photo" style="left:110px;top:585px;background:radial-gradient(circle at 50% 45%,#3d5f8a 0%,#2c4060 22%,#d8cdb8 45%,#8a6a4a 100%)" role="img" aria-label="Cupped hands holding the planet Earth"></div>
  <div class="card-title" style="left:107px;top:934px">Finibus Bonorum et</div>
  <div class="card-photo" style="left:615px;top:585px;background:linear-gradient(180deg,#f2dca0 0%,#e4a740 35%,#c67a18 70%,#9a5a10 100%)" role="img" aria-label="Two men standing together in a golden field"></div>
  <div class="card-title" style="left:613px;top:934px">Finibus Bonorum et</div>
</section>

<section class="testimonial">
  <h2 class="section-title" style="top:2318px">WHAT PEOPLE <span class="accent">SAY ABOUT US</span></h2>
  <p class="abs quote">“Lorem ipsum dolor sit amet, consectetur adipiscing elit, sed do eiusmod tempor incididunt ut labore et dolore magna aliqua. Quis ipsum suspendisse ultrices gravida. Risus commodo viverra maecenas accumsan lacus vel facilisis.psum dolor sit amet, consectetur adipiscing elit, sed do eiusmod tempor incididunt ut labore et dolore magna aliqua. ”</p>
  <div class="abs avatar" role="img" aria-label="Client portrait"></div>
  <div class="abs author">DANIEL REYES<small>Finibus Bonorum</small></div>
  <span class="dot-bar" style="left:486px;width:54px"></span>
  <span class="dot-bar on" style="left:546px;width:52px"></span>
  <span class="dot-bar" style="left:604px;width:52px"></span>
  <span class="dot-bar" style="left:661px;width:53px"></span>
</section>

<section class="contact">
  <div class="contact-bg" role="img" aria-label="Dim background of candles and an open book"></div>
  <h2 class="section-title contact-title">CONTACT US FOR A FREE 15 MINUTE CONSULT</h2>
  <p class="abs contact-lead">Are you looking to make a change, but need some help on where to start?</p>
  <p class="abs contact-sub">Reach out. We offer free 15-minute phone consultations to answer your questions and get you in touch with a therapist who is the right fit for you.</p>
  <div class="field" style="left:202px;top:232px;width:392px;height:43px">Full Name</div>
  <div class="field" style="left:606px;top:232px;width:392px;height:43px">Phone Number</div>
  <div class="field" style="left:202px;top:294px;width:392px;height:43px">Email Address</div>
  <div class="radio" style="left:614px"><i></i>New Client</div>
  <div class="radio" style="left:733px"><i></i>Existing Client</div>
  <div class="field" style="left:202px;top:355px;width:796px;height:100px">Tell us what we can help you with</div>
  <a class="abs btn-outline">Submit</a>
</section>

<footer class="footer"></footer>
<div class="abs foot-mark"></div>
<div class="abs foot-name">THE WILLOW HOURS</div>
<span class="social" style="left:177px" aria-label="Social profile"></span>
<span class="social" style="left:227px" aria-label="Social profile"></span>
<span class="social" style="left:277px" aria-label="Social profile"></span>
<span class="social" style="left:326px" aria-label="Social profile"></span>
<div class="foot-col" style="left:525px">
  <h4>Quick Links</h4>Home<br>About<br>Shop<br>Blog<br>Services<br>Contact
</div>
<div class="foot-col" style="left:701px;line-height:20px">
  <h4 style="margin-bottom:4px">Contact Info</h4>
  <div class="row"><svg width="11" height="14" viewBox="0 0 11 14"><path d="M5.5 0C2.5 0 0 2.4 0 5.4 0 9.3 5.5 14 5.5 14S11 9.3 11 5.4C11 2.4 8.5 0 5.5 0zm0 7.5a2 2 0 110-4 2 2 0 010 4z" fill="#2e1a4a"/></svg><span>48 Linden Lane<br>Fairhaven USA 20417</span></div>
  <div class="row" style="margin-top:12px"><svg width="14" height="14" viewBox="0 0 14 14"><path d="M3 1l2 3-1.3 1.3a8 8 0 005 5L10 9l3 2-1.2 2.2C6.5 13 1 7.5 .8 2.2z" fill="none" stroke="#2e1a4a" stroke-width="1.4"/></svg><span>+1 555 - 014 - 2290</span></div>
  <div class="row" style="margin-top:16px"><svg width="14" height="10" viewBox="0 0 14 10"><rect x=".5" y=".5" width="13" height="9" fill="#2e1a4a"/><path d="M.5 .5L7 6l6.5-5.5" fill="none" stroke="#f4f1ec"/></svg><span>hello@thewillowhours.com</span></div>
</div>
<div class="foot-col" style="left:993px">
  <h4>Support</h4>Privacy Policy<br>Terms of Service<br>Credit<br>FAQ
</div>
<div class="abs foot-rule"></div>
<p class="abs copyright">©Copyright ©2022 The Willow Hours. All Rights Reserved.</p>

</body>
</html>
```